Business Consulting Business Card

professional business card with basic information (1) First and Last name (2) email address, (3) phone number, (4) website.

```html
<!DOCTYPE html>
<html lang="en">
<head>
<meta charset="utf-8">
<title>Tide Harbor Business Card</title>
<link href="https://fonts.googleapis.com/css2?family=Montserrat:wght@400;500&family=Open+Sans:wght@400;600&display=swap" rel="stylesheet">
<style>
  :root {
    --navy: #062540;
    --teal: #4bb5b8;
    --paper: #f7f7f7;
    --ink: #1b1f24;
    --backdrop: #e4e6e8;
  }
  * { margin: 0; padding: 0; box-sizing: border-box; }
  html, body {
    width: 1200px; height: 1021px; overflow: hidden;
    background: var(--backdrop);
  }
  .canvas {
    position: relative; width: 1200px; height: 1021px;
  }
  .card {
    position: absolute; left: 250px; width: 700px; height: 400px;
    overflow: hidden;
    box-shadow: 0 6px 18px rgba(0,0,0,0.18);
  }
  .card--front { top: 70px; background: var(--navy); }
  .card--back { top: 530px; background: var(--paper); }

  .accent-circle {
    position: absolute; border-radius: 50%; background: var(--teal);
  }
  .card--front .accent-circle { width: 300px; height: 300px; left: -120px; top: -10px; }
  .card--back .accent-circle { width: 300px; height: 300px; right: -110px; bottom: -90px; }

  .wordmark {
    font-family: "Montserrat", sans-serif; font-weight: 400;
    text-transform: uppercase; letter-spacing: 0.3em; white-space: nowrap;
  }
  .card--front .wordmark {
    position: absolute; right: 52px; top: 184px;
    font-size: 28px; color: #ffffff;
    margin-right: -0.3em;
  }
  .brand {
    position: absolute; left: 48px; top: 44px;
    display: flex; align-items: center; gap: 14px;
  }
  .brand-dot { width: 40px; height: 40px; border-radius: 50%; background: var(--teal); }
  .card--back .wordmark { font-size: 26px; color: var(--navy); }

  .contact {
    position: absolute; left: 60px; top: 130px;
    font-family: "Open Sans", sans-serif; color: var(--ink);
  }
  .contact-name { font-size: 22px; font-weight: 600; color: var(--teal); line-height: 1.1; }
  .contact-title { font-size: 17px; margin-top: 2px; }
  .contact-rule { width: 46px; height: 2px; background: var(--teal); margin: 14px 0 18px; }
  .contact-list { list-style: none; font-size: 17px; line-height: 1.45; }
  .contact-list li { display: flex; align-items: center; gap: 10px; }
  .contact-list svg { width: 16px; height: 16px; flex: none; }
  .contact-address { font-size: 17px; margin-top: 8px; }
</style>
</head>
<body>
<div class="canvas">
  <section class="card card--front">
    <div class="accent-circle"></div>
    <div class="wordmark">Tide Harbor</div>
  </section>

  <section class="card card--back">
    <div class="accent-circle"></div>
    <div class="brand">
      <div class="brand-dot"></div>
      <div class="wordmark">Tide Harbor</div>
    </div>
    <div class="contact">
      <div class="contact-name">Marcus Ellery</div>
      <div class="contact-title">Managing Broker</div>
      <div class="contact-rule"></div>
      <ul class="contact-list">
        <li>
          <svg viewBox="0 0 16 16" aria-hidden="true"><path fill="#4bb5b8" d="M3.5 1.5l2.4 0 1 3.3-1.6 1.3a8 8 0 0 0 4.6 4.6l1.3-1.6 3.3 1v2.4c0 .8-.7 1.5-1.5 1.5A12 12 0 0 1 2 3c0-.8.7-1.5 1.5-1.5z"/></svg>
          (305) 555-0148
        </li>
        <li>
          <svg viewBox="0 0 16 16" aria-hidden="true"><rect x="1.5" y="3.5" width="13" height="9" fill="none" stroke="#4bb5b8" stroke-width="1.4"/><path d="M1.5 3.5l6.5 5 6.5-5" fill="none" stroke="#4bb5b8" stroke-width="1.4"/></svg>
          hello@tideharbor.com
        </li>
        <li>
          <svg viewBox="0 0 16 16" aria-hidden="true"><g fill="none" stroke="#4bb5b8" stroke-width="1.2"><circle cx="8" cy="8" r="6.3"/><ellipse cx="8" cy="8" rx="2.8" ry="6.3"/><path d="M1.7 8h12.6M2.8 4.8h10.4M2.8 11.2h10.4"/></g></svg>
          www.tideharbor.com
        </li>
      </ul>
      <div class="contact-address">1450 Bayshore Ln, Miami, FL, 33133</div>
    </div>
  </section>
</div>
</body>
</html>
```